Vltavan Pedal Rides company needs new Web Design

We need a new design for our main website. You can find the wireframe(file # 12) for the homepage in uploaded files. Firstly we want a design for the homepage (Please take a look at last uploaded file #12 for more information). If we like it we would also need designs for other subpages (section detail page, tour detail page, reservation form, FAQ, photogallery, search results, blog and basic content page). All wireframes are ready, we need design, graphics, colors ideas.
Our current page is: http://www.kolovrat-jizdy.cz. The logo and information content should remain the same.
Updates

Notes for Kolovrat-jizdy.cz  -new web site 2014

 

There is new file uploaded with notes. Its a draft But Its just square boxes, and boring..we need some creativity, some curves, shapes…. Motions.

Bikes elements could be used, wheel shapes.. 

Web site should show that bikes is the best way of getting around, itsecological, green, fun and healthy. 

The new file is uploaded for more explanation, ideas, layouts and notes.

Reason: We still dont see the good interesting design ideas.

Reason: New updates in uploaded file #12.

We are looking for an exciting  original design; bike parts as chain, wheels, frames, nature elements.. can be used as borders for blocks. Decent background with bike wheel traces, or bike elements, some graphic and fun stuff to show that its not just a bike shop But bike tour company providing fun, active and informational experience!

Also check the updated brief and file#12.

Reason: Not available for close communication from Dec 7 till Dec 13

Reason: Winter holidays

Target Market(s)

Our customers are mostly tourists visiting Prague interested in active, informational and fun way to see the city; including big student and company groups, families, independent travelers; age from 16 to 75. Please take a look at last uploaded file #12 for more information.

Industry/Entity Type

It Company

Requirements
Must have
• Exciting original design, bike parts as chain, wheel.. can be used as borders for blocks. Decent background with bike wheel traces, or bike elements, some graphic and fun stuff to show that its not just a bike shop But bike tour company providing fun, active and informational experience!
Nice to have
• -web visitors should easily see the different kind of services/tours we offer
-impression should be sporty/active but not too much as our services are suitable for people who are not active on daily bases as well using the bike as the way of transportation not as the sport/adrenalin tool.

```html
<!DOCTYPE html>
<html lang="en">
<head>
<meta charset="utf-8">
<title>Vltavan Pedal Rides – Guided Bike Tours &amp; Rentals</title>
<link rel="stylesheet" href="https://fonts.googleapis.com/css2?family=Amaranth:wght@400;700&family=Open+Sans:wght@400;700&family=Ubuntu:wght@500;700&family=Dancing+Script&display=swap">
<style>
  :root {
    --orange: #f07a12;
    --orange-light: #ff9a2e;
    --orange-dark: #d9620a;
    --nav-active: #d55a08;
    --gold-dark: #f4a712;
    --sky-top: #9fd8f5;
    --sky-bottom: #dff3fc;
    --city: #b9ddf1;
    --text: #555;
    --card-border: #dcdcdc;
    --white: #fff;
  }
  * { box-sizing: border-box; margin: 0; padding: 0; }
  html, body { width: 1200px; height: 1000px; overflow: hidden; background: var(--white); }
  body { position: relative; font-family: "Open Sans", Arial, sans-serif; }

  .site-header {
    position: absolute; left: 0; top: 0; width: 1200px; height: 84px; overflow: hidden;
    background: linear-gradient(var(--sky-top), var(--sky-bottom));
  }
  .skyline {
    position: absolute; left: 0; bottom: 0; width: 1200px; height: 74px;
    background:
      radial-gradient(ellipse 90px 40px at 60px 20px, rgba(255,255,255,.9), rgba(255,255,255,0)),
      radial-gradient(ellipse 110px 38px at 330px 18px, rgba(255,255,255,.85), rgba(255,255,255,0)),
      radial-gradient(ellipse 120px 36px at 690px 26px, rgba(255,255,255,.8), rgba(255,255,255,0)),
      radial-gradient(ellipse 100px 34px at 900px 22px, rgba(255,255,255,.8), rgba(255,255,255,0)),
      linear-gradient(to top, var(--city) 0%, #c9e7f7 45%, rgba(201,231,247,0) 100%);
  }
  .trees-left {
    position: absolute; left: 0; bottom: 0; width: 110px; height: 34px;
    background: radial-gradient(ellipse 70px 30px at 45px 34px, #6cc43f, #8fd65c 60%, rgba(143,214,92,0) 100%);
  }
  .skyline-right {
    position: absolute; right: 0; bottom: 0; width: 250px; height: 74px;
    background: linear-gradient(100deg, #f6b634 0%, #f3d35a 22%, #9bd86a 45%, #7fcf8f 62%, #6fc6e8 100%);
    -webkit-mask-image: linear-gradient(90deg, rgba(0,0,0,0) 0%, #000 18%);
            mask-image: linear-gradient(90deg, rgba(0,0,0,0) 0%, #000 18%);
    opacity: .9;
  }
  .brand { position: absolute; left: 175px; top: 12px; display: flex; align-items: center; gap: 10px; }
  .brand-mark { width: 62px; height: 62px; border-radius: 50%; background: var(--orange); }
  .brand-name { font-family: "Ubuntu", sans-serif; font-weight: 700; font-size: 18px; color: var(--orange); line-height: 1; }
  .brand-tagline { font-size: 7.5px; color: #666; letter-spacing: .2px; margin-top: 5px; }
  .riders {
    position: absolute; left: 412px; top: 30px; width: 160px; height: 54px;
    background: radial-gradient(ellipse 80px 28px at 80px 32px, rgba(215,122,58,.75), rgba(233,149,90,.35) 65%, rgba(233,149,90,0) 100%);
  }
  .languages { position: absolute; left: 606px; top: 12px; display: flex; gap: 6px; }
  .languages span { width: 22px; height: 22px; border-radius: 50%; border: 2px solid var(--white); background: #a9c6da; box-shadow: 0 1px 2px rgba(0,0,0,.15); }
  .languages span:first-child { background: #d9e2ef; }
  .search {
    position: absolute; left: 796px; top: 32px; width: 214px; height: 26px; background: var(--white);
    border: 1px solid #b7d7ea; border-radius: 4px; font-size: 9px; color: #888; padding: 7px 12px;
  }
  .search svg { position: absolute; right: 12px; top: 5px; }
  .plane { position: absolute; left: 748px; top: 32px; }

  .main-nav {
    position: absolute; left: 0; top: 84px; width: 1200px; height: 40px;
    background: linear-gradient(var(--orange-light), var(--orange));
    border-bottom: 1px solid var(--orange-dark);
  }
  .main-nav ul { list-style: none; position: absolute; left: 179px; top: 0; display: flex; height: 40px; }
  .main-nav li {
    font-size: 11px; font-weight: 700; color: var(--white); line-height: 40px; text-align: center;
    border-right: 1px solid rgba(0,0,0,.12); text-transform: uppercase;
  }
  .main-nav li.is-active { background: var(--nav-active); }
  .reserve-btn {
    position: absolute; left: 827px; top: 6px; width: 152px; height: 27px;
    background: linear-gradient(#ffd659, var(--gold-dark)); border: 1px solid #e99b0d; border-radius: 3px;
    color: #a24f00; font-size: 11px; font-weight: 700; text-align: center; line-height: 25px; letter-spacing: .4px;
  }

  .hero {
    position: absolute; left: 0; top: 124px; width: 1200px; height: 448px;
    background: linear-gradient(180deg, #6d9fc6 0%, #a8c4d6 40%, #e8b982 70%, #6b6a48 100%);
  }
  .hero-title {
    position: absolute; left: 0; top: 160px; width: 1190px; text-align: center;
    font-family: "Amaranth", sans-serif; font-weight: 700; font-size: 61px; line-height: 76px; color: var(--white);
    text-shadow: 0 2px 4px rgba(0,0,0,.35);
  }
  .hero-sub {
    position: absolute; left: 0; top: 228px; width: 1190px; text-align: center;
    font-family: "Amaranth", sans-serif; font-weight: 700; font-size: 22px; color: var(--white);
    text-shadow: 0 1px 3px rgba(0,0,0,.4);
  }
  .slider-arrow { position: absolute; top: 322px; }
  .video-note {
    position: absolute; left: 866px; top: 405px; width: 155px; text-align: center;
    font-family: "Dancing Script", cursive; font-size: 21px; line-height: 22px; color: var(--orange);
  }
  .laptop { position: absolute; left: 318px; top: 300px; }
  .slider-dots { position: absolute; left: 566px; top: 631px; display: flex; gap: 6px; }
  .slider-dots span { width: 10px; height: 10px; border-radius: 50%; background: #b5b5b5; }
  .slider-dots span.is-active { background: var(--orange); }

  .service-card {
    position: absolute; top: 698px; width: 263px; height: 320px;
    border: 1px solid var(--card-border); border-radius: 3px; background: var(--white);
  }
  .service-photo {
    position: absolute; left: 15px; top: 15px; width: 231px; height: 141px;
    border: 1px solid var(--card-border); padding: 2px; background: var(--white);
  }
  .service-photo div { width: 100%; height: 100%; }
  .service-title {
    position: absolute; left: 15px; top: 163px; font-family: "Ubuntu", sans-serif; font-weight: 500;
    font-size: 15px; color: var(--orange);
  }
  .service-text {
    position: absolute; left: 15px; top: 190px; width: 226px; font-family: Arial, sans-serif;
    font-size: 8.6px; line-height: 18px; color: var(--text);
  }
  .service-link {
    position: absolute; left: -1px; top: 274px; width: 263px; height: 46px;
    background: linear-gradient(var(--orange-light), var(--orange)); color: var(--white);
    font-family: "Ubuntu", sans-serif; font-weight: 500; font-size: 13px; padding: 14px 15px;
  }
  .service-link svg { position: absolute; right: 26px; top: 17px; }
</style>
</head>
<body>
  <header class="site-header">
    <div class="skyline" role="img" aria-label="Light blue cartoon city skyline with white clouds"></div>
    <div class="trees-left" role="img" aria-label="Green cartoon trees"></div>
    <div class="skyline-right" role="img" aria-label="Colourful cartoon skyscrapers and trees"></div>
    <div class="brand">
      <div class="brand-mark"></div>
      <div>
        <div class="brand-name">Vltavan Pedal Rides</div>
        <div class="brand-tagline">GUIDED BIKE TOURS &amp; RENTALS</div>
      </div>
    </div>
    <div class="riders" role="img" aria-label="Orange silhouettes of three cyclists riding"></div>
    <div class="languages" role="img" aria-label="Language selection flags">
      <span></span><span></span><span></span><span></span>
    </div>
    <svg class="plane" width="40" height="22" viewBox="0 0 40 22" aria-hidden="true">
      <path d="M2 12 L36 6 L38 9 L24 13 L30 20 L26 20 L18 14 L8 16 L6 19 L3 19 L5 14 Z" fill="#8fb9d6"/>
    </svg>
    <div class="search">Search here
      <svg width="14" height="14" viewBox="0 0 14 14"><circle cx="6" cy="6" r="4.5" fill="none" stroke="#3a86c1" stroke-width="1.6"/><path d="M9.5 9.5 L13 13" stroke="#3a86c1" stroke-width="1.8"/></svg>
    </div>
  </header>

  <nav class="main-nav">
    <ul>
      <li class="is-active" style="width:72px">Home</li>
      <li style="width:108px">Our Tours</li>
      <li style="width:130px">Private Tours</li>
      <li style="width:80px">About</li>
      <li style="width:71px">Blog</li>
      <li style="width:63px">FAQ</li>
      <li style="width:92px">Contact</li>
    </ul>
    <div class="reserve-btn">RESERVATION</div>
  </nav>

  <section class="hero" role="img" aria-label="Cyclist with a backpack riding at sunset over the city"></section>
  <h1 class="hero-title">Join our ride now</h1>
  <p class="hero-sub">Discover our services, make a reservation.</p>

  <svg class="slider-arrow" style="left:158px" width="22" height="52" viewBox="0 0 22 52" aria-hidden="true">
    <path d="M18 2 L4 26 L18 50" fill="none" stroke="#5f8fb4" stroke-width="4"/>
  </svg>
  <svg class="slider-arrow" style="left:1008px" width="22" height="52" viewBox="0 0 22 52" aria-hidden="true">
    <path d="M4 2 L18 26 L4 50" fill="none" stroke="#f07a12" stroke-width="4"/>
  </svg>

  <svg class="laptop" width="552" height="326" viewBox="0 0 552 326" aria-label="Laptop showing the video presentation">
    <defs>
      <linearGradient id="lid" x1="0" y1="0" x2="0" y2="1"><stop offset="0" stop-color="#2b2b2b"/><stop offset="1" stop-color="#111"/></linearGradient>
      <linearGradient id="base" x1="0" y1="0" x2="0" y2="1"><stop offset="0" stop-color="#eee"/><stop offset="1" stop-color="#9a9a9a"/></linearGradient>
      <linearGradient id="video" x1="0" y1="0" x2="0" y2="1"><stop offset="0" stop-color="#6b5a44"/><stop offset=".5" stop-color="#4c4236"/><stop offset="1" stop-color="#2f2b26"/></linearGradient>
    </defs>
    <rect x="52" y="0" width="448" height="296" rx="12" fill="url(#lid)"/>
    <rect x="68" y="18" width="416" height="256" fill="url(#video)" role="img" aria-label="Video still of a tour group standing with bicycles"/>
    <circle cx="268" cy="144" r="38" fill="rgba(0,0,0,.15)" stroke="rgba(255,255,255,.55)" stroke-width="5"/>
    <path d="M258 128 L284 144 L258 160 Z" fill="rgba(255,255,255,.6)"/>
    <path d="M0 294 H552 L546 306 Q540 312 520 312 H32 Q12 312 6 306 Z" fill="url(#base)"/>
    <rect x="236" y="294" width="80" height="6" rx="3" fill="#bcbcbc"/>
  </svg>

  <div class="video-note">watch our video presentation</div>
  <svg style="position:absolute;left:836px;top:427px" width="40" height="22" viewBox="0 0 40 22" aria-hidden="true">
    <path d="M36 6 Q18 0 6 14" fill="none" stroke="#f07a12" stroke-width="1.5"/>
    <path d="M2 10 L6 16 L12 12" fill="none" stroke="#f07a12" stroke-width="1.5"/>
  </svg>

  <div class="slider-dots"><span></span><span class="is-active"></span><span></span><span></span></div>

  <article class="service-card" style="left:177px">
    <div class="service-photo"><div role="img" aria-label="Tour group with bicycles on a historic town square" style="background:linear-gradient(#9a8a78,#7a7268 60%,#8e8b86)"></div></div>
    <h2 class="service-title">City Tours</h2>
    <p class="service-text">Lorem ipsum dolor sit amet, consectetur adipiscing elit. Vestibulum felis nunc, consequat quis sem et, ornare dapibus odio. Donec sit amet dolor sed odio luctus sit tristique nec et nibh. Integer gravida elit a ante.</p>
    <div class="service-link">Bestseller Tours
      <svg width="8" height="12" viewBox="0 0 8 12"><path d="M1 1 L6 6 L1 11" fill="none" stroke="#fff" stroke-width="2"/></svg>
    </div>
  </article>

  <article class="service-card" style="left:463px">
    <div class="service-photo"><div role="img" aria-label="Cyclists riding a country road between vineyards" style="background:linear-gradient(#aac4dc,#8fa4a6 45%,#6f8a4a 65%,#b8a88a)"></div></div>
    <h2 class="service-title">Country Tours</h2>
    <p class="service-text">Lorem ipsum dolor sit amet, consectetur adipiscing elit. Vestibulum felis nunc, consequat quis sem et, ornare dapibus odio. Donec sit amet dolor sed odio luctus sit tristique nec et nibh. Integer gravida elit a ante.</p>
    <div class="service-link">Recomended Tours
      <svg width="8" height="12" viewBox="0 0 8 12"><path d="M1 1 L6 6 L1 11" fill="none" stroke="#fff" stroke-width="2"/></svg>
    </div>
  </article>

  <article class="service-card" style="left:748px">
    <div class="service-photo"><div role="img" aria-label="Row of rental bicycles parked in docking stations on a street" style="background:linear-gradient(#8e8e8c,#6e6d6a 50%,#9d9b97)"></div></div>
    <h2 class="service-title">Bike Rental</h2>
    <p class="service-text">Lorem ipsum dolor sit amet, consectetur adipiscing elit. Vestibulum felis nunc, consequat quis sem et, ornare dapibus odio. Donec sit amet dolor sed odio luctus sit tristique nec et nibh. Integer gravida elit a ante.</p>
    <div class="service-link">You might also like
      <svg width="8" height="12" viewBox="0 0 8 12"><path d="M1 1 L6 6 L1 11" fill="none" stroke="#fff" stroke-width="2"/></svg>
    </div>
  </article>
</body>
</html>
```